Creative Brochure for Beauty School

We need a brochure designed on legal sized paper (8.5" X 14"), folded in half, and stapled in the middle, to create an 8-page (including covers) project. Therefore, your design for each page should be prepared in 7"x8.5" size (vertical). The brochure should have the look and feel of a magazine (a couple of samples attached to brief files for your reference). Think a magazine published for individuals interested in becoming beauty and wellness professionals. GET CREATIVE! We give you complete creative freedom.

NOTE: FOR DESIGN SELECTION PURPOSES, WE ONLY REQUIRE THE COVER AND 1-2 PAGES. I DO NOT NEED THE COMPLETED BROCHURE, AS I REALIZE TIME IS MONEY. WE WILL WORK TOGETHER TO COMPLETE PROJECT ONCE A DESIGN IS SELECTED.

Our school has been in business for over a decade and provides education in beauty and wellness programs. The purpose of this brochure is to showcase all our program offerings to prospect students in a creative and inspiring way. The brochure will be provided to everyone that inquires about our programs of study and it should provide basic and straightforward information about the school and each program, along with notable facts about us or the industry.

The design should consist of the following elements:

1. Front Cover page. Needs to be beautifully designed and eye catching, having the look and feel of a magazine cover. Cover must have:

- Logo: used as the "magazine’s" masthead
- Tag Line::::::: Beautify your future
-main image (use any of the attached images OR any stock image that can be purchased later by us). Only requirement is that the image has to be of stunning quality.
-Cover lines: (Designers, you may show your creativity). Some ideas on cover lines:
+8 beauty and wellness programs ::::: Endless career opportunities
+Academic Excellence: 82.44% graduation rate in 2012-2013^^
+Affordable tuition and financial assistance programs available.*
+ Miami’s premier choice for beauty education

-any other element desired to enhance the magazine theme.

-Required Disclaimer: (required disclaimers but can and should be very small print)

^^Based on PLOVEM’ 2012-13 Annual Report
*Financial aid available to those who qualify.

2. Must dedicate an area for each of our programs of study. We offer 8 programs, but some can be combined into one page in the layout. The programs can be divided into 2 main categories: beauty programs and spa/wellness programs. The content for each program will be provided later, depending on the design, but we do not expect it to exceed 3-4 sentences of main text for each program. The layout should be easy to read through use of typography, headlines, pull quotes, font colors and hierarchy. The copy should not be lengthy, rather concise and easy to read.

***The beauty programs are:
-Cosmetology (this is the main program so give it the importance it merits in the design)
-Makeup Artistry
-Barber (mainly designed for male students, if images are used, they should be male model)

***Spa/Wellness programs:
-Spa Therapy
-Massage Therapy (can showcase a photo of a male if needed to create diversity)
-Skin Care
-Manicure, Pedicure & Nail Extensions
-Full Specialist (combines the Skin Care and Manicure, Pedicure & Nail Extensions programs)

FYI: Please use the names of the programs verbatim.

3. Areas for (brief) industry content, testimonials (which can include a picture of the individual, to be provided later, should the design require it), facts about the school or industry, and any other idea you come up with.

4. Back cover. Allow area for mailing.

I have added several photos to this brief that you may use as you wish, although some may need Photoshopping. Please use any other photo you want, as long as you have copyrights or if we can buy the rights to the image later. Also added to files, photo of business card and screenshot of website design (no published yet) for color reference.

**This design will require 2 language versions, one in English and one in Spanish. Once a design is selected, we will provide all the necessary text in English and Spanish to allow you to complete.
Updates

Hello everyone:

I have added to the design brief a Microsoft word document with all the (English) text that we need to add to the brochure. I will really appreciate it if you go ahead and prepare a couple of these pages, to match the look and feel of the front cover, using the text and specifications provided in that document. I give you complete freedom in designing the body of the brochure. You may re-arrange the text, as long as you use everything or manage to convey the same message. If you feel that something in the text can be said differently, let me know, or present it. The text is not set in stone, we are open to your creative ideas.

Thanks-

Target Market(s)

Adults 18-49 years, typically our student body in comprised of 70% female / 30% male. The look should be modern, hip yet elegant and sophisticated.

Industry/Entity Type

Education

Requirements
Must have
• Magazine look and feel. Beautiful, eye catching design. We sell beauty, therefore design should be beautiful and glamorous, to go along with the industry.

-include tag line: Beautify your future
-Contact info:
Address: 2916 NW 3rd Avenue. Miami, Fl 33127
Tel: 305-914-3062
Fax: 786-520-4419
www.lunavest.edu
Instagram & Facebook icons / lunavestglowacademy
Should not have
• Should not have a corporate/serious feel or boring look.

```html
<!DOCTYPE html>
<html lang="en">
<head>
<meta charset="utf-8">
<title>Lunavest School of Beauty – Magazine Cover and Mailer</title>
<link rel="stylesheet" href="https://fonts.googleapis.com/css2?family=Arimo:wght@400;700&family=Carlito&display=swap">
<style>
  :root {
    --pink: #e2307f;
    --violet: #9a5aa6;
    --periwinkle: #6a6cb4;
    --ink: #2f2f3a;
    --black: #111;
    --mark: #4b4b55;
    --paper: #ffffff;
    --photo-hair: #7a1e16;
    --photo-dark: #1a1414;
  }
  * { margin: 0; padding: 0; box-sizing: border-box; }
  html, body { width: 1200px; height: 737px; overflow: hidden; background: var(--paper); }
  body { font-family: "Arimo", Arial, sans-serif; color: var(--ink); position: relative; }

  .panel {
    position: absolute; top: 0; height: 737px;
    background: linear-gradient(155deg, var(--pink) 0%, var(--violet) 38%, var(--periwinkle) 75%);
    overflow: hidden;
  }
  .panel--mailing { left: 0; width: 599px; }
  .panel--cover { left: 606px; width: 594px; }

  .abs { position: absolute; line-height: 1; white-space: nowrap; }

  /* mailing side */
  .address-box {
    position: absolute; left: 48px; top: 19px; width: 529px; height: 347px;
    background: var(--paper);
  }
  .postage-box {
    position: absolute; left: 333px; top: 0; width: 196px; height: 99px;
    border: 1px solid var(--black);
    font-size: 25px; color: var(--black);
    display: flex; justify-content: center; padding-top: 36px;
  }
  .recipient { position: absolute; left: 58px; color: var(--black); font-size: 36px; line-height: 1; }
  .recipient--to { top: 89px; font-size: 47px; }
  .recipient--name { top: 148px; }
  .recipient--street { top: 199px; }
  .recipient--city { top: 250px; }
  .recipient--zip { top: 300px; left: 270px; }

  .masthead-name { font-family: "Arimo", Arial, sans-serif; font-weight: 700; color: var(--mark); letter-spacing: 12px; }
  .masthead-sub { font-family: "Carlito", Calibri, sans-serif; color: var(--ink); }

  .tagline { font-weight: 700; color: var(--ink); }
  .contact { font-size: 23px; font-weight: 700; color: var(--ink); }

  /* cover side */
  .program-head { font-size: 13px; font-weight: 700; color: var(--ink); }
  .program { font-size: 15px; font-weight: 700; color: var(--ink); }
  .program--lead { font-size: 23px; font-weight: 400; color: var(--black); }

  .cover-lines { position: absolute; left: 14px; top: 590px; width: 405px; }
  .cover-line { font-size: 11px; font-weight: 700; color: var(--ink); line-height: 1.4; white-space: nowrap; }
  .cover-line strong { color: var(--black); }
  .disclaimers { position: absolute; left: 14px; top: 692px; }
  .disclaimer { font-size: 8.5px; color: var(--ink); line-height: 1.4; white-space: nowrap; }

  .cover-art { position: absolute; left: 0; top: 0; }
  .cover-art text { font-family: "Arimo", Arial, sans-serif; font-weight: 700; fill: var(--black); }
</style>
</head>
<body>

<section class="panel panel--mailing">
  <div class="address-box">
    <div class="postage-box">Postage</div>
    <div class="recipient recipient--to">To:</div>
    <div class="recipient recipient--name">MR John Doe</div>
    <div class="recipient recipient--street">555 SE 25th Street</div>
    <div class="recipient recipient--city">Anytown Any State</div>
    <div class="recipient recipient--zip">555555</div>
  </div>

  <div class="abs masthead-name" style="left:24px; top:396px; font-size:80px;">Lunavest</div>
  <div class="abs masthead-sub" style="left:196px; top:477px; font-size:24px;">SCHOOL OF BEAUTY</div>

  <div class="abs tagline" style="left:138px; top:528px; font-size:25px;">BEAUTIFY YOUR FUTURE</div>

  <div class="abs contact" style="left:27px; top:568px;">Address: 2916 NW 3rd Avenue. Miami, Fl 33127</div>
  <div class="abs contact" style="left:27px; top:601px;">Tel: 305-914-3062</div>
  <div class="abs contact" style="left:27px; top:633px;">Fax: 786-520-4419</div>
  <div class="abs contact" style="left:27px; top:665px;">www.lunavest.edu</div>
</section>

<section class="panel panel--cover">
  <div class="abs masthead-name" style="left:10px; top:26px; font-size:80px;">Lunavest</div>
  <div class="abs masthead-sub" style="left:178px; top:105px; font-size:24px;">SCHOOL OF BEAUTY</div>

  <div class="abs program-head" style="left:23px; top:128px;">Beauty programs</div>
  <div class="abs program program--lead" style="left:5px; top:152px;">Cosmetology</div>
  <div class="abs program" style="left:17px; top:189px;">Makeup Artistry</div>
  <div class="abs program" style="left:49px; top:211px;">Barber</div>

  <svg class="cover-art" width="594" height="737" viewBox="606 0 594 737">
    <defs>
      <radialGradient id="portrait-tone" cx="50%" cy="45%" r="60%">
        <stop offset="0%" stop-color="#c8867a"/>
        <stop offset="45%" stop-color="var(--photo-hair)"/>
        <stop offset="100%" stop-color="var(--photo-dark)"/>
      </radialGradient>
      <path id="tagline-arc" d="M 692 345 A 216 216 0 0 1 1120 345"/>
    </defs>
    <circle cx="906" cy="372" r="200" fill="url(#portrait-tone)" role="img"
            aria-label="Portrait photo of a red-haired model wearing green and teal eye makeup"/>
    <text font-size="27">
      <textPath href="#tagline-arc" startOffset="50%" text-anchor="middle" textLength="430" lengthAdjust="spacing">BEAUTIFY YOUR FUTURE</textPath>
    </text>
  </svg>

  <div class="abs program-head" style="left:424px; top:515px;">Spa/Wellness programs</div>
  <div class="abs program" style="left:424px; top:536px;">Skin Care</div>
  <div class="abs program" style="left:424px; top:558px;">Spa Therapy</div>
  <div class="abs program" style="left:424px; top:580px;">Massage Therapy</div>
  <div class="abs program" style="left:424px; top:602px;">Full Specialist</div>
  <div class="abs program" style="left:424px; top:624px;">Manicure, Pedicure &amp;</div>
  <div class="abs program" style="left:424px; top:643px;">Nail Extensions</div>

  <div class="cover-lines">
    <p class="cover-line"><strong>8 beauty and wellness programs</strong> · Endless career opportunities</p>
    <p class="cover-line"><strong>Academic Excellence:</strong> 82.44% graduation rate in 2012-2013^^</p>
    <p class="cover-line">Affordable tuition and financial assistance programs available.*</p>
    <p class="cover-line"><strong>Miami’s premier choice for beauty education</strong></p>
  </div>

  <div class="disclaimers">
    <p class="disclaimer">^^Based on PLOVEM’ 2012-13 Annual Report</p>
    <p class="disclaimer">*Financial aid available to those who qualify.</p>
  </div>
</section>

</body>
</html>
```